Classy business card for accounting firm

We're looking for a new business card for our accounting firm. Our logo was designed by Brandolith, so all of the design info we would like to use has been provided. The specific font provided isn't required to be used.

We want the card to look classy and elegent. Probably more minimalistic, but still with some pops of color.

The options we would like to include on the card are as follows:
1. Main office phone line
2. Direct phone line
3. Email address
4. Website URL
5. Name
6. Title (CEO, President, etc.)
7. Firm Address

The design and card should be double sided!!! The drop down box in the project brief for some reason is defaulting to single sided. Not sure why this is happening.

Thanks!

Contact Information for Business Card

The options we would like to include on the card are as follows: 1. Main office phone line 2. Direct phone line 3. Email address 4. Website URL 5. Name 6. Title (CEO, President, etc.) 7. Firm Address

Requirements
Must have
• Card must be double sided.

```html
<!DOCTYPE html>
<html lang="en">
<head>
<meta charset="utf-8">
<title>Ledgerline Associates – Business Card</title>
<link href="https://fonts.googleapis.com/css2?family=Lato:wght@400;700;900&display=swap" rel="stylesheet">
<style>
  :root {
    --bg: #2c2f34;
    --card-white: #ffffff;
    --card-grey: #656565;
    --orange: #ff7a00;
    --green: #b5bf35;
    --gold: #e6b800;
    --ink: #3a3a3a;
    --ink-soft: #555555;
    --on-dark: #ffffff;
  }
  * { box-sizing: border-box; margin: 0; padding: 0; }
  html, body { width: 1200px; height: 952px; overflow: hidden; }
  body {
    background: var(--bg);
    display: flex;
    align-items: center;
    justify-content: center;
    gap: 60px;
    font-family: "Lato", sans-serif;
  }
  .card {
    width: 525px;
    height: 300px;
    border-radius: 22px;
    position: relative;
    overflow: hidden;
    box-shadow: 0 14px 30px rgba(0,0,0,.45);
  }

  /* Back side */
  .card--back {
    background: var(--card-grey);
    display: flex;
    align-items: center;
    justify-content: center;
  }
  .firm-name {
    display: flex;
    align-items: center;
    gap: 12px;
    font-family: "Lato", sans-serif;
    font-weight: 700;
    font-size: 30px;
    color: var(--on-dark);
  }
  .firm-name__dot {
    width: 14px; height: 14px;
    border-radius: 50%;
    background: var(--orange);
  }

  /* Front side */
  .card--front { background: var(--card-white); color: var(--ink); }
  .brand {
    position: absolute;
    left: 30px;
    top: 30px;
    display: flex;
    align-items: center;
    gap: 8px;
    font-family: "Lato", sans-serif;
    font-weight: 700;
    font-size: 16px;
    color: var(--ink);
  }
  .brand__dot { width: 10px; height: 10px; border-radius: 50%; background: var(--orange); }

  .contacts {
    position: absolute;
    left: 30px;
    top: 118px;
    list-style: none;
    font-size: 11.5px;
    line-height: 1.35;
    color: var(--ink);
  }
  .contacts li { display: flex; gap: 9px; margin-bottom: 7px; }
  .icon {
    flex: none;
    width: 16px; height: 16px;
    border-radius: 3px;
    display: flex; align-items: center; justify-content: center;
  }
  .icon--orange { background: var(--orange); }
  .icon--green { background: var(--green); }
  .icon svg { width: 10px; height: 10px; fill: none; stroke: #fff; stroke-width: 1.4; stroke-linecap: round; stroke-linejoin: round; }

  .person {
    position: absolute;
    right: 30px;
    top: 112px;
    text-align: right;
  }
  .person__name {
    font-weight: 900;
    font-size: 20px;
    letter-spacing: 1px;
    text-transform: uppercase;
  }
  .person__first { color: var(--orange); }
  .person__last { color: var(--green); }
  .person__title {
    font-size: 13px;
    color: var(--ink-soft);
    margin-top: 2px;
  }
  .person__rule { display: inline-block; width: 60px; height: 2px; margin-top: 4px; background: var(--gold); }
</style>
</head>
<body>

  <section class="card card--back" aria-label="Card back">
    <div class="firm-name"><span class="firm-name__dot"></span>Ledgerline Associates</div>
  </section>

  <section class="card card--front" aria-label="Card front">
    <div class="brand"><span class="brand__dot"></span>Ledgerline Associates</div>

    <ul class="contacts">
      <li>
        <span class="icon icon--orange"><svg viewBox="0 0 10 10"><path d="M5 9 C2 6 2 5 2 4 a3 3 0 0 1 6 0 c0 1 0 2 -3 5z"/><circle cx="5" cy="4" r="0.8"/></svg></span>
        <span>2170 Harbor View Avenue<br>Arlington, VA 22201</span>
      </li>
      <li>
        <span class="icon icon--green"><svg viewBox="0 0 10 10"><path d="M2 1.5 l2 0 l0.8 2 l-1.2 1 a5 5 0 0 0 2 2 l1-1.2 l2 0.8 l0 2 a7 7 0 0 1 -6.6-6.6z"/></svg></span>
        <span>+1 202 555 0148</span>
      </li>
      <li>
        <span class="icon icon--green"><svg viewBox="0 0 10 10"><rect x="1" y="2" width="8" height="6"/><path d="M1 2 l4 3.5 l4-3.5"/></svg></span>
        <span>hello@ledgerlinetax.com</span>
      </li>
      <li>
        <span class="icon icon--green"><svg viewBox="0 0 10 10"><circle cx="5" cy="5" r="3.8"/><path d="M1.2 5 h7.6 M5 1.2 c-2 2.5 -2 5 0 7.6 M5 1.2 c2 2.5 2 5 0 7.6"/></svg></span>
        <span>www.ledgerlinetax.com</span>
      </li>
    </ul>

    <div class="person">
      <div class="person__name"><span class="person__first">Daniel R.</span> <span class="person__last">Whitford</span></div>
      <div class="person__title">Managing Director</div>
      <span class="person__rule"></span>
    </div>
  </section>

</body>
</html>
```